Launch Invite for LUMEN in hand-drawn chalk style

Looking for an invitation for the launch of LUMEN a creative marketing collaborative founded by Gloria Pembrook. We are a marketing consultancy firm. We are fun, quirky and do things a little different. The launch party will have a silent auction to benefit the charity Guarding Our Prairies. The auction will be a photography show feature local photographers with the theme of Texas natural resources and wildlife. Event will be Wednesday, May 22 from 6:30 to 9:30p at Harlow Gallery located at 514 North 9th, Austin, Texas

Please see the attached verbiage for invite text. Words in bold indicate importance.

We want a chalkboard art invitation similar to the style of Mira Koslowe. So just a black chalkboard background with white chalk text.

http://www.mirakoslowe-example.com/chalk/

Target Market(s)

freinds, family, small business owners, influencers, non-profits

Industry/Entity Type

Charity

Requirements
Must have
• Love the style of the Nora Belden piece on Mira's Website.
Or nagging image or wedding couples image.
chalkboard invite with chalk text
fun, looks like its going to be a good time.
Nice to have
• Highlight lumen, date, time, location, charity

```html
<!DOCTYPE html>
<html lang="en">
<head>
<meta charset="utf-8">
<title>LUMEN Launch Invitation</title>
<link href="https://fonts.googleapis.com/css2?family=Rye&family=Cinzel:wght@400;700&family=Kaushan+Script&family=Kalam:wght@400;700&family=Caveat:wght@400;600&display=swap" rel="stylesheet">
<style>
  :root {
    --board-light: #3b3b3b;
    --board-dark: #1c1c1c;
    --chalk: #f1f1ec;
    --chalk-soft: rgba(241, 241, 236, 0.82);
    --chalk-faint: rgba(241, 241, 236, 0.16);
    --ribbon-top: rgba(200, 200, 196, 0.34);
    --ribbon-bottom: rgba(200, 200, 196, 0.16);
  }
  html, body {
    margin: 0;
    padding: 0;
    width: 860px;
    height: 1200px;
    overflow: hidden;
    background: var(--board-dark);
  }
  .invite {
    display: block;
    width: 860px;
    height: 1200px;
    background: radial-gradient(ellipse at 50% 40%, var(--board-light) 0%, #2a2a2a 55%, var(--board-dark) 100%);
  }
  .frame-line { fill: none; stroke: var(--chalk-soft); }
  .chalk { fill: var(--chalk); }
  .greeting-small { font-family: "Cinzel", serif; font-size: 17px; letter-spacing: 2px; }
  .greeting-city { font-family: "Cinzel", serif; font-weight: 700; font-size: 34px; letter-spacing: 2px; }
  .ribbon-area { fill: url(#ribbonTone); }
  .flourish-area { fill: var(--chalk-faint); }
  .brand-name { font-family: "Rye", serif; font-size: 84px; letter-spacing: 4px; fill: #fdfdfa; }
  .founded-by { font-family: "Kaushan Script", cursive; font-size: 30px; }
  .founder { font-family: "Kalam", cursive; font-size: 50px; }
  .collective { font-family: "Kalam", cursive; font-weight: 700; font-size: 38px; }
  .services-lead { font-family: "Kaushan Script", cursive; font-size: 32px; }
  .service { font-family: "Caveat", cursive; font-size: 30px; }
  .celebrate { font-family: "Rye", serif; font-size: 58px; letter-spacing: 3px; fill: #fdfdfa; }
  .event-date { font-family: "Kalam", cursive; font-weight: 700; font-size: 46px; }
  .event-time { font-family: "Kalam", cursive; font-size: 26px; }
  .venue { font-family: "Kalam", cursive; font-weight: 700; font-size: 40px; }
  .city { font-family: "Kalam", cursive; font-weight: 700; font-size: 36px; }
  .feature { font-family: "Kaushan Script", cursive; font-size: 27px; }
  .story { font-family: "Caveat", cursive; font-size: 25px; }
  .charity-name { font-family: "Kalam", cursive; font-size: 22px; }
  .footer-note { font-family: "Caveat", cursive; font-size: 23px; }
</style>
</head>
<body>
<svg class="invite" viewBox="0 0 860 1200" xmlns="http://www.w3.org/2000/svg">
  <defs>
    <linearGradient id="ribbonTone" x1="0" y1="0" x2="0" y2="1">
      <stop offset="0" stop-color="var(--ribbon-top)"/>
      <stop offset="1" stop-color="var(--ribbon-bottom)"/>
    </linearGradient>
  </defs>

  <!-- border -->
  <rect class="frame-line" x="14" y="14" width="832" height="1172" stroke-width="3"/>
  <rect class="frame-line" x="26" y="26" width="808" height="1148" stroke-width="1.5"/>

  <!-- greeting -->
  <text class="chalk greeting-small" x="430" y="42" text-anchor="middle">HELLO</text>
  <text class="chalk greeting-city" x="430" y="80" text-anchor="middle">AUSTIN!</text>
  <text class="chalk greeting-small" x="430" y="116" text-anchor="middle">INTRODUCING</text>

  <!-- brand ribbon -->
  <rect class="ribbon-area" role="img" aria-label="Hand-drawn chalk ribbon banner behind the brand name"
        x="140" y="148" width="580" height="124"/>
  <text class="brand-name" x="430" y="240" text-anchor="middle">LUMEN</text>

  <!-- founder -->
  <text class="chalk founded-by" x="430" y="318" text-anchor="middle">founded by</text>
  <text class="chalk founder" x="430" y="368" text-anchor="middle">Gloria Pembrook</text>
  <text class="chalk collective" x="430" y="414" text-anchor="middle">Creative Marketing Collaborative</text>
  <rect class="flourish-area" role="img" aria-label="Chalk swirl flourish" x="250" y="432" width="360" height="30"/>

  <!-- services -->
  <text class="chalk services-lead" x="430" y="505" text-anchor="middle">crafting brands for</text>
  <g class="chalk service">
    <text x="268" y="548">small business</text>
    <text x="268" y="579">non-profits</text>
    <text x="268" y="610">start ups</text>
    <text x="268" y="641">social media</text>
    <text x="476" y="548">marketing</text>
    <text x="476" y="579">strategy</text>
    <text x="476" y="610">design</text>
    <text x="476" y="641">PR</text>
  </g>
  <rect class="flourish-area" role="img" aria-label="Chalk scroll flourish" x="190" y="660" width="480" height="26"/>

  <!-- celebrate banner -->
  <rect class="ribbon-area" role="img" aria-label="Chalk banner behind the word celebrate"
        x="170" y="710" width="520" height="72"/>
  <text class="celebrate" x="430" y="766" text-anchor="middle">CELEBRATE</text>

  <!-- date and place -->
  <text class="chalk event-date" x="430" y="828" text-anchor="middle">Wednesday, May 22</text>
  <text class="chalk event-time" x="430" y="860" text-anchor="middle">6:30 to 9:30 pm</text>
  <text class="chalk venue" x="430" y="906" text-anchor="middle">Harlow Gallery, 514 North 9th</text>
  <text class="chalk city" x="430" y="948" text-anchor="middle">Austin, Texas</text>

  <!-- features -->
  <text class="chalk feature" x="90" y="996">Texas Photography Gallery</text>
  <path class="chalk" d="M430 976 L435 988 L448 988 L438 996 L442 1009 L430 1001 L418 1009 L422 996 L412 988 L425 988 Z"/>
  <text class="chalk feature" x="500" y="996">Silent Auction benefiting</text>

  <!-- story -->
  <g class="chalk story" text-anchor="end">
    <text x="340" y="1040">Started by Helen Marsh to</text>
    <text x="340" y="1068">benefit communities, build on</text>
    <text x="340" y="1096">all Texans</text>
  </g>
  <g class="chalk story">
    <text x="522" y="1040">to spur conservation efforts that</text>
    <text x="522" y="1068">the success of others, and inspire</text>
    <text x="522" y="1096">all to join in.</text>
  </g>

  <!-- charity -->
  <text class="chalk charity-name" x="430" y="1058" text-anchor="middle">Guarding Our</text>
  <text class="chalk charity-name" x="430" y="1086" text-anchor="middle">Prairies</text>

  <!-- footer -->
  <text class="chalk footer-note" x="90" y="1150">Info: gloria@lumengroup.com</text>
  <text class="chalk footer-note" x="522" y="1150">Attire: Keep Austin Stylish</text>
</svg>
</body>
</html>
```